Business Card needed for Drainor, a growing Septic Service company

Drainor, a growing local septic service company in Pennsylvania, needs updated business cards. We'd like the business card to feature our logo and communicate that we provide Septic Pumping, Installations/Repairs, Restroom Rentals, and 24/7 Emergency Service. The business card should be eye-catching, bold, and clean/simple. We have been in business almost 10 years and would like to expand and update our business brand and image.

Target Market(s)

Residential and Commercial, New and Current Homeowners

Industry/Entity Type

Service

Contact Information for Business Card

Contact on the business card should be: Dean Harlow Owner & Operator
Phone: 610-555-0187
Email: service@drainor-example.com
Website: www.drainor-example.com
Address: 812 Millbrook Lane Brookvale PA 17990

Font styles to use
Sans Serif

Colors

Designer to choose colors to be used in the design.

Requirements
Must have
• Feature logo on both side of business card.
Nice to have
• We envision the contact information on one side and our services listed on the other side. Utilize the green from the symbol in our logo as part of the design, overall design color scheme should be white, grey, black.

```html
<!DOCTYPE html>
<html lang="en">
<head>
<meta charset="utf-8">
<title>Drainor Business Card</title>
<link href="https://fonts.googleapis.com/css2?family=Arimo:wght@400;700&family=Krona+One&display=swap" rel="stylesheet">
<style>
  :root {
    --green: #7dc242;
    --green-light: #92d74e;
    --green-dark: #6aab35;
    --white: #ffffff;
    --black: #111111;
    --grey-line: #c9c9c9;
    --page: #e6e7e8;
  }
  * { margin: 0; padding: 0; box-sizing: border-box; }
  html, body { width: 1200px; height: 1015px; overflow: hidden; }
  body {
    background: var(--page);
    font-family: "Arimo", Arial, sans-serif;
    position: relative;
  }
  .card {
    position: absolute;
    left: 220px;
    width: 760px;
    height: 434px;
    overflow: hidden;
    box-shadow: 0 6px 18px rgba(0,0,0,0.18);
  }
  /* Front */
  .card-front { top: 40px; background: var(--green); }
  .front-texture {
    position: absolute; inset: 0;
    background: linear-gradient(135deg, var(--green-light) 0%, var(--green) 50%, var(--green-dark) 100%);
  }
  .front-brand {
    position: absolute; left: 50%; top: 50%;
    transform: translate(-50%, -50%);
    display: flex; align-items: center; gap: 18px;
  }
  .brand-square { width: 46px; height: 46px; background: var(--white); }
  .brand-name {
    font-family: "Arimo", Arial, sans-serif; font-weight: 700;
    text-transform: uppercase; white-space: nowrap;
  }
  .front-brand .brand-name { font-size: 64px; letter-spacing: 4px; color: var(--white); }
  /* Back */
  .card-back { top: 534px; background: var(--white); }
  .back-brand {
    position: absolute; left: 48px; top: 138px;
    display: flex; align-items: center; gap: 14px;
  }
  .back-brand .brand-square { background: var(--green); width: 40px; height: 40px; }
  .back-brand .brand-name { font-size: 52px; letter-spacing: 3px; color: var(--black); }
  .divider {
    position: absolute; left: 400px; top: 40px;
    width: 1px; height: 230px; background: var(--grey-line);
  }
  .contact { position: absolute; left: 430px; top: 48px; color: var(--black); }
  .contact-name {
    font-family: "Krona One", Arial, sans-serif; font-size: 21px;
    color: var(--green); text-transform: uppercase; letter-spacing: 1px; white-space: nowrap;
  }
  .contact-title { font-size: 18px; margin: 4px 0 12px; }
  .contact-lines { padding-left: 10px; }
  .contact-line { display: flex; align-items: center; gap: 10px; font-size: 17px; line-height: 26px; white-space: nowrap; }
  .contact-line svg { width: 16px; height: 16px; flex: none; fill: var(--green); }
  .contact-line .accent { color: var(--green); }
  .address { margin-top: 12px; padding-left: 36px; font-size: 18px; line-height: 24px; }
  .services-band {
    position: absolute; left: 0; right: 0; top: 290px; height: 108px;
    background: var(--green); color: var(--white);
    display: flex; flex-direction: column; justify-content: center; align-items: center;
    font-size: 21px; line-height: 30px; letter-spacing: 0.5px; text-transform: uppercase;
  }
</style>
</head>
<body>
  <section class="card card-front">
    <div class="front-texture" role="img" aria-label="Tiled grid of brand symbols in shades of green"></div>
    <div class="front-brand">
      <span class="brand-square"></span>
      <span class="brand-name">Drainor</span>
    </div>
  </section>

  <section class="card card-back">
    <div class="back-brand">
      <span class="brand-square"></span>
      <span class="brand-name">Drainor</span>
    </div>
    <div class="divider"></div>
    <div class="contact">
      <div class="contact-name">Dean Harlow</div>
      <div class="contact-title">Owner &amp; Operator</div>
      <div class="contact-lines">
        <div class="contact-line">
          <svg viewBox="0 0 16 16"><path d="M3.5 1l2.5 3-1.5 1.8c.9 2 2.5 3.6 4.5 4.5L10.8 8.8 14 11.2l-1.5 3c-6.4-.4-11.1-5.1-11.5-11.5z"/></svg>
          <span>610-555-0187</span>
        </div>
        <div class="contact-line">
          <svg viewBox="0 0 16 16"><path d="M1 3h14v10H1z M1.5 3.5L8 9l6.5-5.5" fill="none" stroke="#7dc242" stroke-width="1.6"/></svg>
          <span>service@drainor-example.com</span>
        </div>
        <div class="contact-line">
          <svg viewBox="0 0 16 16"><circle cx="8" cy="8" r="6.5" fill="none" stroke="#7dc242" stroke-width="1.5"/><path d="M1.5 8h13M8 1.5c-3 3.5-3 9.5 0 13M8 1.5c3 3.5 3 9.5 0 13" fill="none" stroke="#7dc242" stroke-width="1.2"/></svg>
          <span>www.<span class="accent">drainor-example</span>.com</span>
        </div>
      </div>
      <div class="address">812 Millbrook Lane<br>Brookvale PA 17990</div>
    </div>
    <div class="services-band">
      <span>Septic Pumping &bull; Installations/Repairs</span>
      <span>Restroom Rentals &bull; 24/7 Emergency Service</span>
    </div>
  </section>
</body>
</html>
```